Kit com 6 Layouts de Post para Redes Sociais (Facebook, Instagram e etc) + Capa de Facebookpara RZ SEGUROS E CONSORCIOS
Postado por: gestao.rzseguros_2840395726   Estou Offline

```html
<!DOCTYPE html>
<html lang="pt-BR">
<head>
<meta charset="UTF-8">
<title>Post – Seu Texto Aqui</title>
<link href="https://fonts.googleapis.com/css2?family=Poppins:wght@400;500;600;700&display=swap" rel="stylesheet">
<style>
  :root {
    --purple-top: #a457bb;
    --purple-mid: #7b3f9e;
    --purple-deep: #3f2a6b;
    --accent-pink: #d57be0;
    --label-pink: #e08ce8;
    --white: #ffffff;
    --icon-dark: #5a2d7a;
    --photo-warm: #c9a89a;
    --photo-red: #a8493a;
    --photo-light: #e9e2de;
  }
  * { margin: 0; padding: 0; box-sizing: border-box; }
  html, body { width: 1200px; height: 1200px; overflow: hidden; }
  body { font-family: 'Poppins', sans-serif; }
  .post {
    position: relative;
    width: 1200px;
    height: 1200px;
    overflow: hidden;
    background: linear-gradient(170deg, var(--purple-top) 0%, var(--purple-mid) 45%, var(--purple-deep) 100%);
  }
  .post__shapes { position: absolute; inset: 0; }
  .brand-placeholder {
    position: absolute;
    left: 60px;
    top: 122px;
    font-size: 38px;
    font-weight: 500;
    color: var(--white);
    letter-spacing: 0.5px;
  }
  .headline {
    position: absolute;
    left: 60px;
    top: 282px;
    font-size: 76px;
    line-height: 88px;
    font-weight: 600;
    color: var(--white);
    letter-spacing: -1px;
  }
  .contact {
    position: absolute;
    left: 88px;
    top: 1032px;
    color: var(--white);
  }
  .contact__label {
    margin-left: 74px;
    font-size: 17px;
    font-weight: 500;
    color: var(--label-pink);
    text-transform: uppercase;
    line-height: 22px;
  }
  .contact__phone {
    display: flex;
    align-items: center;
    gap: 14px;
    margin-top: 4px;
  }
  .contact__dot {
    width: 30px; height: 30px; border-radius: 50%;
    background: var(--label-pink);
    display: flex; align-items: center; justify-content: center;
  }
  .contact__prefix { font-size: 19px; font-weight: 500; }
  .contact__number { font-size: 29px; font-weight: 700; margin-left: -6px; line-height: 36px; }
  .contact__social {
    display: flex; align-items: center; gap: 10px;
    margin-top: 2px; margin-left: 50px;
    font-size: 16px; font-weight: 500;
  }
  .contact__social-dot {
    width: 18px; height: 18px; border-radius: 50%;
    background: var(--label-pink);
  }
</style>
</head>
<body>
<main class="post">
  <svg class="post__shapes" width="1200" height="1200" viewBox="0 0 1200 1200">
    <defs>
      <linearGradient id="photoTone" x1="0" y1="0" x2="1" y2="1">
        <stop offset="0" stop-color="var(--photo-light)"/>
        <stop offset="0.45" stop-color="var(--photo-red)"/>
        <stop offset="0.8" stop-color="var(--photo-warm)"/>
        <stop offset="1" stop-color="var(--photo-light)"/>
      </linearGradient>
    </defs>
    <path class="photo-area" role="img"
          aria-label="Foto: pessoa idosa assinando um documento com caneta, apoiada por outra mão"
          d="M530 77 H1200 V1200 H1052 L500 130 Q480 88 530 77 Z"
          fill="url(#photoTone)"/>
    <path class="accent-line" d="M0 696 H540 Q620 696 660 770 L910 1200"
          fill="none" stroke="var(--accent-pink)" stroke-width="3"/>
  </svg>

  <div class="brand-placeholder">SUA LOGO</div>

  <h1 class="headline">Seu<br>Texto Aqui<br>Seu texto<br>aqui.</h1>

  <div class="contact">
    <div class="contact__label">Ligue agora</div>
    <div class="contact__phone">
      <span class="contact__dot">
        <svg width="16" height="16" viewBox="0 0 24 24"><path d="M6.6 10.8a15 15 0 0 0 6.6 6.6l2.2-2.2c.3-.3.7-.4 1-.2 1.1.4 2.3.6 3.6.6.6 0 1 .4 1 1V20c0 .6-.4 1-1 1A17 17 0 0 1 3 4c0-.6.4-1 1-1h3.5c.6 0 1 .4 1 1 0 1.3.2 2.5.6 3.6.1.3 0 .7-.2 1z" fill="var(--icon-dark)"/></svg>
      </span>
      <span class="contact__prefix">xx.</span>
      <span class="contact__number">0000.0000</span>
    </div>
    <div class="contact__social">
      <span class="contact__social-dot"></span>
      <span class="contact__handle">@SEUPERFIL</span>
    </div>
  </div>
</main>
</body>
</html>
```